Need a creative postcard for corporate client gifts baskets

We need a nice looking, fun and whimsical card to enclose with our Easter client gifts. We are a high-end audiovisual business that specializes in awards shows, galas and events for event producers, corporate entities and government agencies.We will have small baskets assembled with a variety of different chocolates and candies that everyone enjoyed as children.The card must include our logo and our website address (www.velmarstage.example). We'd entertain fun ideas that integrate our business and an Easter bunny such as a bunny wearing an intercom headset and working an audio console. Other ideas are definitely welcome; please note we are NOT a DJ company...we are very professional business who execute corporate events at the highest level. Visit www.velmarstage.example to get a better sense of our brand. Also attached are samples of the cards we've done the last 2 years.

Target Market(s)

Corporate, Government, Association

Font styles to use
Sans Serif

Colors
85acd3
fbf289
e34197

Requirements
Should not have
• DJ, consumer, home audio visual references

```html
<!DOCTYPE html>
<html lang="en">
<head>
<meta charset="utf-8">
<title>Velmar Stage – Happy Easter Card</title>
<link href="https://fonts.googleapis.com/css2?family=Bungee+Inline&family=Lato:wght@400;700;900&display=swap" rel="stylesheet">
<style>
  :root {
    --backdrop: #322828;
    --card-white: #ffffff;
    --wash-blue: #cfe4f3;
    --wash-pink: #f6d9ea;
    --wash-yellow: #fbf5c8;
    --brand-ink: #1e1e1e;
    --greeting-pink: #d81b63;
    --string-tan: #d9a77e;
    --egg-yellow: #f2f12c;
    --egg-green: #a8e04a;
    --egg-pink: #f77f9e;
    --grass-green: #4f9a1e;
    --grass-dark: #2f6b12;
    --bunny-blue: #8fa7cf;
    --bunny-orange: #f07a22;
    --url-white: #ffffff;
  }
  * { margin: 0; padding: 0; box-sizing: border-box; }
  html, body {
    width: 1200px; height: 1200px; overflow: hidden;
    background: var(--backdrop);
    font-family: "Lato", sans-serif;
  }
  .card {
    position: absolute; left: 268px; top: 110px;
    width: 666px; height: 980px; overflow: hidden;
    background:
      radial-gradient(ellipse at 25% 10%, var(--wash-pink) 0%, transparent 45%),
      radial-gradient(ellipse at 85% 15%, var(--wash-blue) 0%, transparent 50%),
      radial-gradient(ellipse at 10% 70%, var(--wash-blue) 0%, transparent 45%),
      radial-gradient(ellipse at 90% 70%, var(--wash-yellow) 0%, transparent 40%),
      var(--card-white);
  }
  .egg-pattern {
    position: absolute; left: 0; top: 210px; width: 666px; height: 620px;
    background: radial-gradient(ellipse at 50% 45%, rgba(246,200,225,0.45) 0%, rgba(200,225,240,0.35) 55%, transparent 80%);
  }
  .hanging-eggs { position: absolute; inset: 0; width: 666px; height: 980px; }
  .brand {
    position: absolute; left: 170px; top: 73px;
    display: flex; align-items: center; gap: 14px;
    color: var(--brand-ink);
  }
  .brand-dot {
    width: 96px; height: 96px; border-radius: 50%;
    border: 4px solid var(--brand-ink);
  }
  .brand-name { font-weight: 900; font-size: 46px; line-height: 1; letter-spacing: -0.5px; }
  .brand-tag { font-weight: 400; font-size: 19px; letter-spacing: 9px; margin-top: 4px; }
  .bunny-art {
    position: absolute; left: 112px; top: 206px; width: 444px; height: 452px;
    border-radius: 46% 46% 12% 12%;
    background: linear-gradient(170deg, var(--bunny-blue) 0%, #b9c9e3 40%, var(--bunny-orange) 72%, #3b3f48 100%);
    opacity: 0.85;
  }
  .greeting {
    position: absolute; left: 0; width: 666px; top: 686px;
    text-align: center; padding-left: 60px;
    font-family: "Bungee Inline", sans-serif;
    font-size: 74px; line-height: 1; letter-spacing: -2px;
    color: var(--greeting-pink);
    white-space: nowrap;
  }
  .egg-meadow {
    position: absolute; left: 0; top: 806px; width: 666px; height: 174px;
    background:
      linear-gradient(90deg, #f0a12a, #e3264a, #9ccc3a, #f28a1c, #7fbf2a, #e3264a, #f2b01c),
      var(--grass-green);
    background-size: 100% 92px, 100% 100%;
    background-repeat: no-repeat;
  }
  .egg-meadow::after {
    content: ""; position: absolute; left: 0; right: 0; top: 80px; bottom: 0;
    background: linear-gradient(180deg, var(--grass-green) 0%, var(--grass-dark) 100%);
  }
  .website {
    position: absolute; left: 0; width: 666px; top: 928px;
    text-align: center; color: var(--url-white);
    font-size: 22px; letter-spacing: 3px; font-weight: 400;
  }
</style>
</head>
<body>
  <main class="card">
    <div class="egg-pattern" role="img" aria-label="Faint decorated Easter egg pattern in pastel colours"></div>

    <svg class="hanging-eggs" viewBox="0 0 666 980">
      <g stroke="var(--string-tan)" stroke-width="3">
        <line x1="28" y1="0" x2="28" y2="250"/>
        <line x1="56" y1="0" x2="56" y2="420"/>
        <line x1="92" y1="0" x2="92" y2="140"/>
        <line x1="578" y1="0" x2="578" y2="140"/>
        <line x1="610" y1="0" x2="610" y2="420"/>
        <line x1="634" y1="0" x2="634" y2="250"/>
      </g>
      <g role="img" aria-label="Hanging decorated Easter eggs">
        <ellipse cx="92" cy="182" rx="37" ry="48" fill="var(--egg-yellow)"/>
        <ellipse cx="28" cy="298" rx="37" ry="50" fill="var(--egg-green)"/>
        <ellipse cx="56" cy="466" rx="42" ry="55" fill="var(--egg-pink)"/>
        <ellipse cx="578" cy="182" rx="37" ry="48" fill="var(--egg-yellow)"/>
        <ellipse cx="634" cy="298" rx="37" ry="50" fill="var(--egg-green)"/>
        <ellipse cx="610" cy="466" rx="42" ry="55" fill="var(--egg-pink)"/>
      </g>
    </svg>

    <header class="brand">
      <div class="brand-dot"></div>
      <div>
        <div class="brand-name">Velmar Stage</div>
        <div class="brand-tag">audiovisual</div>
      </div>
    </header>

    <div class="bunny-art" role="img" aria-label="Illustration of a cheerful Easter bunny in headphones and an orange shirt at an audio console"></div>

    <h1 class="greeting">HAPPY EASTER</h1>

    <div class="egg-meadow" role="img" aria-label="Row of painted Easter eggs sitting in green grass"></div>

    <p class="website">www.velmarstage.example</p>
  </main>
</body>
</html>
```